Accounting firm needing business card / letterhead designed
Marcus L. Tembrook, CPA
marcus@lumenfiledesk.com
www.lumenfiledesk.com
482 E Larkin Ave Fenwick Bay, ME 04099
555-214-0172
Business

```html
<!DOCTYPE html>
<html lang="en">
<head>
<meta charset="utf-8">
<title>Lumen FileDesk — Business Card</title>
<link href="https://fonts.googleapis.com/css2?family=Roboto:wght@400;500&family=Roboto+Condensed:wght@700&family=Montserrat:wght@600&display=swap" rel="stylesheet">
<style>
  :root {
    --navy: #2b2a6e;
    --green: #8dc63f;
    --white: #ffffff;
    --stage: #e6e4df;
  }
  * { margin: 0; padding: 0; box-sizing: border-box; }
  html, body { width: 900px; height: 1200px; overflow: hidden; }
  body { background: var(--stage); position: relative; font-family: "Roboto", sans-serif; }

  .card {
    position: absolute;
    width: 734px;
    height: 429px;
    border-radius: 22px;
    overflow: hidden;
    box-shadow: 0 6px 18px rgba(0,0,0,0.25);
  }

  /* Front */
  .card-front { left: 88px; top: 133px; background: var(--white); }
  .card-front .marker {
    position: absolute; left: 0; top: 74px; width: 16px; height: 17px; background: var(--green);
  }
  .card-front .holder-name {
    position: absolute; left: 47px; top: 69px;
    font-family: "Roboto Condensed", sans-serif; font-weight: 700;
    font-size: 21px; color: var(--navy); letter-spacing: 0.3px; white-space: nowrap;
  }
  .card-front .wordmark {
    position: absolute; right: 52px; top: 72px;
    font-family: "Roboto Condensed", sans-serif; font-weight: 700;
    font-size: 40px; color: var(--navy); letter-spacing: 1px; text-transform: uppercase; white-space: nowrap;
  }
  .card-front .rule {
    position: absolute; left: 47px; top: 284px; width: 634px; height: 1.5px; background: var(--navy);
  }
  .contact-list {
    position: absolute; left: 47px; top: 296px; list-style: none;
  }
  .contact-list li {
    display: flex; align-items: center; height: 28.5px;
    font-size: 18px; color: var(--navy); white-space: nowrap;
  }
  .contact-list svg { width: 22px; height: 20px; margin-right: 8px; }
  .card-front .address {
    position: absolute; right: 49px; top: 356px;
    font-size: 18px; color: var(--navy); white-space: nowrap;
  }
  .card-front .accent-bar {
    position: absolute; left: 372px; bottom: 0; width: 310px; height: 20px; background: var(--green);
  }

  /* Back */
  .card-back {
    left: 82px; top: 630px;
    background: linear-gradient(180deg, var(--navy) 0%, #2e3a6c 55%, #4f7d55 72%, var(--green) 84%, var(--green) 100%);
  }
  .card-back .wordmark {
    position: absolute; left: 0; right: 0; top: 180px; text-align: center;
    font-family: "Roboto Condensed", sans-serif; font-weight: 700;
    font-size: 58px; color: var(--white); letter-spacing: 2px; text-transform: uppercase; white-space: nowrap;
  }
  .card-back .site {
    position: absolute; left: 0; right: 0; top: 370px; text-align: center;
    font-family: "Montserrat", sans-serif; font-weight: 600;
    font-size: 20px; color: var(--white); letter-spacing: 0.5px;
  }
</style>
</head>
<body>

<section class="card card-front">
  <span class="marker"></span>
  <h1 class="holder-name">MARCUS L. TEMBROOK, CPA</h1>
  <div class="wordmark">Lumen FileDesk</div>
  <div class="rule"></div>
  <ul class="contact-list">
    <li>
      <svg viewBox="0 0 22 20" aria-hidden="true"><path fill="#8dc63f" d="M2 7c0-3 4-5 9-5s9 2 9 5v1h-5V6.5c-1-.6-2.5-.9-4-.9s-3 .3-4 .9V8H2zM5 9h12l2 9H3zM11 11a3 3 0 1 0 0 6 3 3 0 0 0 0-6z"/></svg>
      555-214-0172
    </li>
    <li>
      <svg viewBox="0 0 22 20" aria-hidden="true"><rect x="2" y="4" width="18" height="13" fill="#8dc63f"/><path d="M2 4l9 7 9-7" fill="none" stroke="#fff" stroke-width="1.5"/></svg>
      marcus@lumenfiledesk.com
    </li>
    <li>
      <svg viewBox="0 0 22 20" aria-hidden="true"><g fill="none" stroke="#8dc63f" stroke-width="1.6"><circle cx="11" cy="10" r="8.5"/><ellipse cx="11" cy="10" rx="3.8" ry="8.5"/><path d="M2.5 10h17M4 5.5h14M4 14.5h14"/></g></svg>
      www.lumenfiledesk.com
    </li>
  </ul>
  <p class="address">482 E Larkin Ave Fenwick Bay, ME 04099</p>
  <span class="accent-bar"></span>
</section>

<section class="card card-back">
  <div class="wordmark">Lumen FileDesk</div>
  <p class="site">www.lumenfiledesk.com</p>
</section>

</body>
</html>
```